Flyer/Brochure for a Young Non-Profit

We want to revamp our flyer to complement our new logo and to reflect a greater global appeal. Our company is a non-profit that exchanges students, interns and volunteers across the globe.

We are looking for the following elements:
1. Elegance
2. Brevity
3. Vibrancy
4. Inspirational

We are looking for the following layouts:
1. Single gate-fold, or
2. Die-cut Z Fold
(http://www.foldmerrow.net/15-brochure-fold-types/)

The final design should also look good as a single jpeg or pdf as an email attachment.

The flyer will be given to both our potential young participants and the senior management of our partners.

Please use the uploaded as materials for content (01 word doc and assortment of photos).

Target Market(s)

Students from 15 and above to adults up to 30 years of age. Senior management of commercial companies and other non-profit organizations.

Industry/Entity Type

Non-Profit

Font styles to use
Serif

Requirements
Must have
• Attached contents.

```html
<!DOCTYPE html>
<html lang="en">
<head>
<meta charset="utf-8">
<title>Lumora Art &amp; Exchange – Z-Fold Brochure</title>
<link href="https://fonts.googleapis.com/css2?family=Arimo:wght@400;700&family=Dancing+Script:wght@600&display=swap" rel="stylesheet">
<style>
  :root{
    --stage:#2b2d31;
    --paper:#f4f4f4;
    --white:#ffffff;
    --sky:#1aa9ec;
    --sun:#ffcb1f;
    --ink:#333333;
    --ink-soft:#555555;
    --rule:#444444;
    --accent-red:#e8252b;
    --chip:#2a9de0;
  }
  *{margin:0;padding:0;box-sizing:border-box}
  html,body{width:1200px;height:878px;overflow:hidden}
  body{background:var(--stage);font-family:"Arimo",Arial,sans-serif;position:relative}

  .spread{position:absolute;top:242px;width:560px;height:395px}
  .spread--inside{left:30px;clip-path:polygon(0 0,560px 197px,560px 395px,0 395px)}
  .spread--outside{left:610px;clip-path:polygon(0 199px,560px 0,560px 395px,0 395px)}

  .collage{display:block;width:560px;height:395px}

  .panel{position:absolute;top:0;height:395px;width:187px}
  .panel--contact{left:0;background:var(--paper)}
  .panel--story{left:187px;width:186px;background:var(--sky)}
  .panel--cover{left:373px;background:var(--white)}

  .contact{position:absolute;left:0;width:187px;top:206px;text-align:center;color:var(--ink)}
  .contact__title{font-size:8.5px;font-weight:700;letter-spacing:.2px}
  .contact__title::after{content:"";display:block;width:36px;height:1px;background:var(--rule);margin:4px auto 6px}
  .office{font-size:4.6px;line-height:6.2px;color:var(--ink-soft)}
  .office__name{font-size:7px;color:var(--ink);margin-bottom:2px}
  .contact__rule{width:120px;height:1px;background:var(--rule);margin:5px auto 5px}
  .contact__mail{display:flex;align-items:center;justify-content:center;gap:8px;font-size:5.5px;color:var(--ink)}

  .story{position:absolute;left:16px;width:154px;top:138px;color:var(--white);text-align:center;font-size:4.6px;line-height:6.6px}
  .story p{margin-bottom:6px}
  .social{position:absolute;left:48px;top:352px;list-style:none;color:var(--white);font-size:4.6px;line-height:7px}
  .social li{display:flex;align-items:center;gap:5px}
  .social li::before{content:"";width:4.5px;height:4.5px;background:var(--white);border-radius:1px}

  .cover__brand{position:absolute;right:18px;top:34px;display:flex;align-items:center;gap:5px}
  .cover__brand-dot{width:14px;height:14px;border-radius:50%;background:var(--sky)}
  .cover__brand-name{font-size:9px;font-weight:700;color:var(--ink);line-height:9px}
  .cover__url{position:absolute;left:22px;top:76px;font-size:5px;color:var(--ink)}
  .cover__url::before{content:"";position:absolute;left:-2px;top:-5px;width:62px;height:1px;background:var(--rule)}
  .cover__tagline{position:absolute;left:0;width:187px;top:95px;text-align:center;font-family:"Dancing Script",cursive;font-size:12px;color:var(--accent-red)}

  .band{position:absolute;left:0;width:187px;text-align:center}
  .band--mission{top:125px;height:36px;background:var(--sky);color:var(--white);font-size:4.8px;line-height:6.5px;padding:11px 16px 0}
  .band--vision{top:161px;height:36px;background:var(--sun);color:var(--ink);font-size:4.8px;line-height:6.5px;padding:11px 14px 0}
  .band--programs{top:197px;height:114px;background:var(--sky);color:var(--white);padding-top:13px}
  .band--partners{top:311px;height:84px;background:var(--sun);color:var(--ink);padding-top:9px}
  .band__title{font-size:8.5px;font-weight:700;margin-bottom:8px}
  .programs{list-style:none;text-align:left;padding-left:34px;font-size:4.6px;line-height:10.5px}
  .programs li{display:flex;align-items:center;gap:5px}
  .programs li::before{content:"";border-left:4px solid var(--sun);border-top:2.5px solid transparent;border-bottom:2.5px solid transparent}
  .partners{list-style:none;text-align:left;padding-left:48px}
  .partners li{display:flex;align-items:center;gap:8px;font-size:4.4px;line-height:5.5px;margin-bottom:7px}
  .partners__badge{flex:none;width:18px;height:18px;background:var(--chip)}
</style>
</head>
<body>

<section class="spread spread--inside" aria-label="Brochure inside spread">
  <svg class="collage" viewBox="0 0 560 395" role="img" aria-label="Collage of round photos: students, volunteers, children at play and an elephant encounter, framed by blue, red and yellow rings">
    <defs>
      <linearGradient id="collageTone" x1="0" y1="0" x2="1" y2="1">
        <stop offset="0" stop-color="#b9a78e"/>
        <stop offset=".5" stop-color="#6f8a5a"/>
        <stop offset="1" stop-color="#8d9a86"/>
      </linearGradient>
    </defs>
    <rect width="560" height="395" fill="url(#collageTone)"/>
    <circle cx="74" cy="97" r="74" fill="#c9b7a4" stroke="#1aa9ec" stroke-width="4"/>
    <circle cx="185" cy="175" r="84" fill="#8f7a5e" stroke="#e8252b" stroke-width="5"/>
    <circle cx="316" cy="150" r="72" fill="#9aa7b2" stroke="#1aa9ec" stroke-width="4"/>
    <circle cx="70" cy="300" r="92" fill="#6d6a5c" stroke="#ffcb1f" stroke-width="5"/>
    <circle cx="268" cy="318" r="88" fill="#c7a893" stroke="#ffcb1f" stroke-width="5"/>
    <circle cx="440" cy="300" r="96" fill="#7f9a6e" stroke="#e8252b" stroke-width="5"/>
  </svg>
</section>

<section class="spread spread--outside" aria-label="Brochure outside spread">
  <div class="panel panel--contact">
    <div class="contact">
      <h2 class="contact__title">CONTACT DETAILS</h2>
      <div class="office">
        <p class="office__name">Singapore Office</p>
        <p>#07-12 K, 48 Harbourlight Walk</p>
        <p>Marina Court 4</p>
        <p>Singapore 700482</p>
        <p>Tel: +65 6100 4821</p>
        <p>Email: sg@lumora-exchange.org</p>
      </div>
      <div class="contact__rule"></div>
      <div class="office">
        <p class="office__name">China Office</p>
        <p>上海市虹桥路88号</p>
        <p>枫林苑1202室</p>
        <p>邮编：200150</p>
        <p>电话：+86-021-60001234</p>
        <p>传真：+86-021-60005678</p>
      </div>
      <div class="contact__rule"></div>
      <p class="contact__mail">
        <svg width="11" height="7" viewBox="0 0 11 7" aria-hidden="true"><rect x=".5" y=".5" width="10" height="6" fill="none" stroke="#333"/><path d="M.5 .5 5.5 4 10.5 .5" fill="none" stroke="#333"/></svg>
        hello@lumora-exchange.org
      </p>
    </div>
  </div>

  <div class="panel panel--story">
    <div class="story">
      <p>Founded in 2005, Lumora Art and Culture Exchange works with trusted partners across 23 countries from our offices in Singapore and Shanghai.</p>
      <p>From country to country, our interns and volunteers serve in hospitals, schools, reef diving, wildlife and environmental care, and humanitarian and social community work.</p>
      <p>Our host partners and participants have reaped many benefits through matching needs and skills. Be it helping heal an injured bird, or guiding young change-makers, each moment shared is a gift of time and attention that helps people, families and animals breathe a little easier and smile a bit more.</p>
      <p>Join us here at Lumora to open minds and touch hearts across the globe.</p>
    </div>
    <ul class="social">
      <li>Lumora Art and Culture Exchange</li>
      <li>@lumora_sg</li>
      <li>@lumora_travel</li>
      <li>lumora.hub</li>
    </ul>
  </div>

  <div class="panel panel--cover">
    <div class="cover__brand">
      <span class="cover__brand-dot"></span>
      <span class="cover__brand-name">LUMORA</span>
    </div>
    <p class="cover__url">www.lumora-exchange.org</p>
    <p class="cover__tagline">Opening Minds, Touching Hearts</p>

    <div class="band band--mission">Grow people and bridges of understanding and cooperation between cultures across the world.</div>
    <div class="band band--vision">A world more at peace and in harmony through cultural appreciation, education and learning.</div>
    <div class="band band--programs">
      <h3 class="band__title">OUR PROGRAMS</h3>
      <ul class="programs">
        <li>International Volunteer Program</li>
        <li>International Internship Program</li>
        <li>International High School Exchange Program</li>
        <li>Group Student Program</li>
        <li>Independent Home Stays</li>
        <li>Language Courses</li>
      </ul>
    </div>
    <div class="band band--partners">
      <h3 class="band__title">ORGANIZATION PARTNERS</h3>
      <ul class="partners">
        <li><span class="partners__badge"></span>Council for Cultural<br>Living Exchange</li>
        <li><span class="partners__badge"></span>Partners in<br>Global Service</li>
      </ul>
    </div>
  </div>
</section>

</body>
</html>
```